PELDRAX Business Cards

We require a business card for our company that provides IT consulting services. We already have a logo that needs to be used on the card. We want a clean professional looking design that incorporates our colours. Our main focus is providing managed services to business, which involves us looking after all of their IT requirements including managing servers/networks, projects, and procurement.

Industry/Entity Type

Information Technology

Requirements
Must have
• our logo, contact information, name, title, phone numbers

```html
<!DOCTYPE html>
<html lang="en">
<head>
<meta charset="utf-8">
<title>PELDRAX Business Cards</title>
<link href="https://fonts.googleapis.com/css2?family=Montserrat:wght@500&family=Roboto:wght@400;700&family=Open+Sans:wght@400&display=swap" rel="stylesheet">
<style>
  :root {
    --backdrop: #b5b5b7;
    --brand-blue: #229fd3;
    --brand-blue-deep: #1f8fc8;
    --accent-gold: #e8b660;
    --card-white: #f6f6f6;
    --text-grey: #6b6b6b;
    --text-dark: #4a4a4a;
  }
  * { margin: 0; padding: 0; box-sizing: border-box; }
  html, body { width: 1200px; height: 1200px; overflow: hidden; }
  body { background: var(--backdrop); position: relative; }

  .card { position: absolute; }

  .card-front {
    left: 322px; top: 262px; width: 554px; height: 317px;
    background: linear-gradient(180deg, #23a3d5 0%, var(--brand-blue-deep) 100%);
    display: flex; align-items: center; justify-content: center; gap: 16px;
  }
  .brand-dot-front {
    width: 40px; height: 40px; border-radius: 50%; background: #ffffff;
  }
  .brand-name-front {
    font-family: "Montserrat", sans-serif; font-weight: 500;
    font-size: 58px; letter-spacing: 4px; color: #ffffff; line-height: 1;
  }

  .card-back {
    left: 331px; top: 664px; width: 535px; height: 306px;
    background: var(--card-white);
  }
  .name-block {
    position: absolute; left: 33px; top: 22px; height: 56px;
    border-left: 8px solid var(--accent-gold); padding-left: 8px;
  }
  .person-name {
    font-family: "Roboto", sans-serif; font-weight: 700;
    font-size: 27px; color: var(--brand-blue-deep); line-height: 32px;
  }
  .person-title {
    font-family: "Roboto", sans-serif; font-weight: 400;
    font-size: 16px; color: var(--text-grey); line-height: 20px;
  }
  .brand-rule {
    position: absolute; top: 126px; height: 8px; background: var(--brand-blue-deep);
  }
  .brand-rule.left { left: 0; width: 265px; }
  .brand-rule.right { left: 509px; right: 0; }
  .brand-back {
    position: absolute; left: 276px; top: 106px; width: 228px; height: 48px;
    display: flex; align-items: center; gap: 10px;
  }
  .brand-dot-back {
    width: 26px; height: 26px; border-radius: 50%; background: var(--brand-blue-deep);
  }
  .brand-name-back {
    font-family: "Montserrat", sans-serif; font-weight: 500;
    font-size: 36px; letter-spacing: 2px; color: var(--brand-blue-deep); line-height: 1;
  }

  .contact-list {
    position: absolute; left: 32px; top: 208px; list-style: none;
    font-family: "Open Sans", sans-serif; font-size: 12px; color: var(--text-dark);
  }
  .contact-item { display: flex; align-items: flex-start; line-height: 18px; margin-bottom: 1px; }
  .contact-icon { width: 12px; height: 12px; margin-top: 3px; margin-right: 10px; flex: none; fill: var(--brand-blue-deep); }
</style>
</head>
<body>

<section class="card card-front" aria-label="Business card front">
  <span class="brand-dot-front"></span>
  <span class="brand-name-front">PELDRAX</span>
</section>

<section class="card card-back" aria-label="Business card back">
  <div class="name-block">
    <p class="person-name">MARA QUILL</p>
    <p class="person-title">Business Development Manager</p>
  </div>

  <div class="brand-rule left"></div>
  <div class="brand-back">
    <span class="brand-dot-back"></span>
    <span class="brand-name-back">PELDRAX</span>
  </div>
  <div class="brand-rule right"></div>

  <ul class="contact-list">
    <li class="contact-item">
      <svg class="contact-icon" viewBox="0 0 12 12"><path d="M6 0a4.2 4.2 0 0 0-4.2 4.2C1.8 7.4 6 12 6 12s4.2-4.6 4.2-7.8A4.2 4.2 0 0 0 6 0zm0 5.9a1.7 1.7 0 1 1 0-3.4 1.7 1.7 0 0 1 0 3.4z"/></svg>
      <span>48 Cedar Lane<br>Box 602, Fernbrook, AB</span>
    </li>
    <li class="contact-item">
      <svg class="contact-icon" viewBox="0 0 12 12"><path d="M2.4 0.5l2 2.3-1.1 1.5c.8 1.7 2.2 3.1 3.9 3.9l1.5-1.1 2.3 2-1.2 1.9C5.3 11 1 6.7.5 1.7z"/></svg>
      <span>+403-555-0188</span>
    </li>
    <li class="contact-item">
      <svg class="contact-icon" viewBox="0 0 12 12"><path d="M0 2h12v1.2L6 7 0 3.2zM0 4.6l6 3.8 6-3.8V10H0z"/></svg>
      <span>info@peldrax.com</span>
    </li>
    <li class="contact-item">
      <svg class="contact-icon" viewBox="0 0 12 12" fill="none"><g stroke="#1f8fc8" stroke-width="1.1" fill="none"><circle cx="6" cy="6" r="5"/><ellipse cx="6" cy="6" rx="2.2" ry="5"/><path d="M1 6h10M2 3.2h8M2 8.8h8"/></g></svg>
      <span>www.peldrax.com</span>
    </li>
  </ul>
</section>

</body>
</html>
```